Business card for femtech company

Nothing too elaborate but elegant and geared towards the mother and baby market. Prefer full-bleed with logo (attached) rear.

```html
<!DOCTYPE html>
<html lang="en">
<head>
<meta charset="utf-8">
<title>Nuvela Business Card</title>
<link rel="stylesheet" href="https://fonts.googleapis.com/css2?family=Montserrat:wght@400;500;600&display=swap">
<style>
  :root {
    --teal: #56c4b8;
    --teal-light: #66cbbf;
    --ink: #2b2b2b;
    --grey: #9a9a9a;
    --rule: #b5b5b5;
    --paper: #ffffff;
    --backdrop: #e9ebeb;
  }
  * { box-sizing: border-box; margin: 0; padding: 0; }
  html, body {
    width: 1200px; height: 1200px; overflow: hidden;
    background: var(--backdrop);
    font-family: "Montserrat", sans-serif;
  }
  .sheet {
    width: 1200px; height: 1200px;
    display: flex; flex-direction: column; align-items: center; justify-content: center;
    gap: 56px;
  }
  .card {
    position: relative;
    width: 900px; height: 514px;
    border-radius: 34px;
    overflow: hidden;
  }
  .card--front { background: var(--paper); }
  .card--back {
    background: linear-gradient(100deg, var(--teal) 0%, var(--teal-light) 45%, var(--teal) 100%);
    display: flex; align-items: center; justify-content: center;
  }

  .brand { display: flex; align-items: center; gap: 26px; }
  .brand__dot { width: 74px; height: 74px; border-radius: 50%; background: var(--teal); }
  .brand__name {
    font-weight: 500; font-size: 88px; letter-spacing: 1px; color: var(--teal); line-height: 1;
  }
  .card--front .brand { position: absolute; left: 150px; top: 120px; }

  .card--back .brand__dot { width: 120px; height: 120px; background: var(--paper); }
  .card--back .brand__name { font-size: 136px; color: var(--paper); }

  .divider {
    position: absolute; left: 470px; top: 290px;
    width: 1px; height: 130px; background: var(--rule);
  }

  .identity { position: absolute; left: 150px; bottom: 74px; }
  .identity__name {
    font-weight: 600; font-size: 44px; letter-spacing: 0.5px; color: var(--teal); line-height: 1;
  }
  .identity__role {
    margin-top: 6px; font-weight: 400; font-size: 26px; letter-spacing: 0.5px; color: var(--ink);
  }

  .contact {
    position: absolute; left: 505px; top: 278px;
    list-style: none; display: flex; flex-direction: column; gap: 9px;
    font-size: 19px; color: var(--ink); letter-spacing: 0.3px;
  }
  .contact__item { display: flex; align-items: flex-start; gap: 12px; line-height: 1.25; }
  .contact__icon { width: 20px; height: 20px; flex: none; fill: var(--teal); margin-top: 2px; }
</style>
</head>
<body>
<main class="sheet">
  <section class="card card--front" aria-label="Card front">
    <div class="brand">
      <span class="brand__dot"></span>
      <span class="brand__name">nuvela</span>
    </div>

    <div class="divider"></div>

    <ul class="contact">
      <li class="contact__item">
        <svg class="contact__icon" viewBox="0 0 24 24"><path d="M6.6 10.8a15.1 15.1 0 0 0 6.6 6.6l2.2-2.2c.3-.3.7-.4 1-.2 1.1.4 2.3.6 3.6.6.6 0 1 .4 1 1V20c0 .6-.4 1-1 1A17 17 0 0 1 3 4c0-.6.4-1 1-1h3.5c.6 0 1 .4 1 1 0 1.3.2 2.5.6 3.6.1.3 0 .7-.2 1z"/></svg>
        <span>(000) 000 0000</span>
      </li>
      <li class="contact__item">
        <svg class="contact__icon" viewBox="0 0 24 24"><path d="M2 5h20v14H2z" fill="none"/><path d="M2 5h20v2l-10 6L2 7zM2 9l10 6 10-6v10H2z"/></svg>
        <span>email@company.com</span>
      </li>
      <li class="contact__item">
        <svg class="contact__icon" viewBox="0 0 24 24"><path d="M12 2a10 10 0 1 0 0 20 10 10 0 0 0 0-20zm6.9 6h-3a15 15 0 0 0-1.3-3.9A8 8 0 0 1 18.9 8zM12 4c.9 1.2 1.6 2.6 2 4h-4c.4-1.4 1.1-2.8 2-4zM4.3 14a8 8 0 0 1 0-4h3.4a16 16 0 0 0 0 4zm.8 2h3a15 15 0 0 0 1.3 3.9A8 8 0 0 1 5.1 16zm3-8h-3a8 8 0 0 1 4.3-3.9A15 15 0 0 0 8.1 8zM12 20c-.9-1.2-1.6-2.6-2-4h4c-.4 1.4-1.1 2.8-2 4zm2.3-6H9.7a14 14 0 0 1 0-4h4.6a14 14 0 0 1 0 4zm.3 5.9a15 15 0 0 0 1.3-3.9h3a8 8 0 0 1-4.3 3.9zm1.7-5.9a16 16 0 0 0 0-4h3.4a8 8 0 0 1 0 4z"/></svg>
        <span>www.company.com</span>
      </li>
      <li class="contact__item">
        <svg class="contact__icon" viewBox="0 0 24 24"><path d="M12 2a7 7 0 0 0-7 7c0 5.2 7 13 7 13s7-7.8 7-13a7 7 0 0 0-7-7zm0 9.5a2.5 2.5 0 1 1 0-5 2.5 2.5 0 0 1 0 5z"/></svg>
        <span>123 Name Street, 000<br>Your City, 00000-000</span>
      </li>
    </ul>

    <div class="identity">
      <p class="identity__name">FULL NAME</p>
      <p class="identity__role">POSITION</p>
    </div>
  </section>

  <section class="card card--back" aria-label="Card back">
    <div class="brand">
      <span class="brand__dot"></span>
      <span class="brand__name">nuvela</span>
    </div>
  </section>
</main>
</body>
</html>
```